Wholesale Fashion Agent

Industry/Entity Type

Fashion

Contact Information for Business Card

I have attached the previous logo, we are wanting to re-vamp with black and white only. Sharp and more modern.

Mirela Stonecroft Agencies back of card
address (to be advised, as we are moving)

MS Agencies front of card, with Fashion Agent on the front

```html
<!DOCTYPE html>
<html lang="en">
<head>
<meta charset="utf-8">
<title>Mirela Stonecroft Agencies – Business Card</title>
<link rel="stylesheet" href="https://fonts.googleapis.com/css2?family=EB+Garamond:wght@400&family=Arimo:wght@400;700&family=Tinos:wght@700&display=swap">
<style>
  :root {
    --ink: #000000;
    --paper: #ffffff;
    --grey: #9a9a9a;
    --grey-soft: #6e6e6e;
    --label: #222222;
  }
  * { box-sizing: border-box; margin: 0; padding: 0; }
  html, body { width: 891px; height: 1200px; overflow: hidden; background: var(--paper); }
  .canvas { position: relative; width: 891px; height: 1200px; }

  .card { position: absolute; left: 0; width: 891px; background: var(--ink); color: var(--paper); }
  .card--face { top: 0; height: 548px; }
  .card--back { top: 600px; height: 460px; }

  .brand-mark { position: absolute; display: flex; align-items: center; gap: 16px; }
  .brand-mark__square { width: 34px; height: 34px; background: var(--grey); flex: none; }
  .brand-mark__name { font-family: "EB Garamond", serif; font-weight: 400; color: var(--paper); white-space: nowrap; }
  .card--face .brand-mark { left: 36px; top: 150px; }
  .card--face .brand-mark__name { font-size: 42px; }
  .card--back .brand-mark { left: 40px; top: 780px; top: 180px; }
  .card--back .brand-mark__name { font-size: 54px; }

  .agency-title { position: absolute; left: 300px; top: 46px; font-family: "EB Garamond", serif; font-size: 41px; font-weight: 400; letter-spacing: 0.5px; }

  .agent-block { position: absolute; left: 590px; top: 150px; width: 240px; }
  .agent-block__name, .agent-block__role { font-family: "Arimo", sans-serif; font-variant: small-caps; text-align: center; padding: 6px 0; }
  .agent-block__name { font-weight: 700; font-size: 27px; color: var(--paper); border-bottom: 2px solid var(--paper); }
  .agent-block__role { font-weight: 400; font-size: 27px; color: var(--grey); border-bottom: 2px solid var(--paper); }

  .splash-band { position: absolute; left: 0; top: 292px; width: 891px; height: 40px;
    background: linear-gradient(90deg, rgba(255,255,255,0.85), rgba(255,255,255,0.55) 60%, rgba(255,255,255,0.15)); }
  .portrait-art { position: absolute; left: 555px; top: 335px; width: 290px; height: 165px;
    background: radial-gradient(ellipse at 40% 50%, #d8d8d8 0%, #5a5a5a 55%, var(--ink) 100%); }

  .contact-list { position: absolute; left: 45px; top: 356px; list-style: none; font-family: "Arimo", sans-serif; font-size: 21px; line-height: 30px; }

  .card-label { position: absolute; left: 0; width: 891px; text-align: center; font-family: "Tinos", serif; font-weight: 700; font-size: 26px; color: var(--label); }
  .card-label--face { top: 558px; }
  .card-label--back { top: 1158px; }

  .back-title { position: absolute; left: 400px; top: 178px; width: 450px; text-align: center; font-family: "EB Garamond", serif; font-size: 42px; line-height: 64px; }
  .back-web { position: absolute; left: 42px; top: 424px; font-family: "Arimo", sans-serif; font-size: 18px; }

  .address-strip { position: absolute; left: 0; top: 1066px; width: 891px; text-align: center; font-family: "EB Garamond", serif; font-size: 25px; color: var(--ink); }
  .base-bar { position: absolute; left: 0; top: 1112px; width: 891px; height: 40px; background: var(--ink); }
</style>
</head>
<body>
<main class="canvas">
  <section class="card card--face" aria-label="Card face">
    <div class="brand-mark">
      <span class="brand-mark__square"></span>
      <span class="brand-mark__name">MS Agencies</span>
    </div>
    <h1 class="agency-title">Mirela Stonecroft Agencies</h1>
    <div class="agent-block">
      <p class="agent-block__name">Mirela Stonecroft</p>
      <p class="agent-block__role">Fashion Agent</p>
    </div>
    <div class="splash-band" role="img" aria-label="White paint splatter stroke across the card"></div>
    <ul class="contact-list">
      <li>P: 07-3100 4821</li>
      <li>F: 07-3100 4822</li>
      <li>M: 0400 555 217</li>
      <li>E: mirela@msagencies.com.au</li>
      <li>W: www.msagencies.com.au</li>
    </ul>
    <div class="portrait-art" role="img" aria-label="Splattered white fashion portrait illustration"></div>
  </section>
  <p class="card-label card-label--face">FACE</p>

  <section class="card card--back" aria-label="Card back">
    <div class="brand-mark">
      <span class="brand-mark__square"></span>
      <span class="brand-mark__name">MS Agencies</span>
    </div>
    <h2 class="back-title">Mirela Stonecroft<br>Agencies</h2>
    <p class="back-web">www.msagencies.com.au</p>
  </section>
  <p class="address-strip">Unit 4/12 Harlow Lane West End Qld 4101 Australia</p>
  <div class="base-bar"></div>
  <p class="card-label card-label--back">BACK</p>
</main>
</body>
</html>
```